Corvane Building Materials letterhead template

Simple but professional letterhead template for business communication.
LOGO/name in upper left, balanced by company contact info on right upper.
Subject description, date...
addressee, cc: and BC: if applicable editable info..

Need extra days to review

```html
<!DOCTYPE html>
<html lang="en">
<head>
<meta charset="utf-8">
<title>Corvane Building Materials – Letterhead</title>
<link rel="stylesheet" href="https://fonts.googleapis.com/css2?family=Rubik:wght@700&family=Tinos&display=swap">
<style>
  :root {
    --brand-blue: #045dbf;
    --swoosh-dark: #343233;
    --page: #fdfdfd;
    --watermark: #dde8f6;
    --signature-tone: #eeeeee;
    --on-blue: #ffffff;
  }
  * { margin: 0; padding: 0; box-sizing: border-box; }
  html, body { width: 917px; height: 1200px; overflow: hidden; background: var(--page); }
  .letterhead { position: relative; width: 917px; height: 1200px; background: var(--page); overflow: hidden; }
  .waves { position: absolute; inset: 0; width: 917px; height: 1200px; }

  .brand { position: absolute; left: 50px; top: 104px; display: flex; align-items: center; gap: 18px; }
  .brand-mark { width: 102px; height: 102px; background: var(--brand-blue); border-radius: 18px; flex: none; }
  .brand-name {
    font-family: "Rubik", sans-serif; font-weight: 700; font-size: 33px; line-height: 41px;
    letter-spacing: 2px; color: var(--brand-blue); text-transform: uppercase;
  }

  .contact {
    position: absolute; left: 662px; top: 20px; height: 120px;
    border-left: 1px solid var(--on-blue); padding-left: 12px;
    font-family: "Tinos", serif; font-style: normal; font-size: 16px; line-height: 20px; color: var(--on-blue);
    letter-spacing: 0.2px;
  }
  .contact-item { display: flex; align-items: flex-start; gap: 10px; margin-bottom: 3px; }
  .contact-item svg { width: 12px; height: 12px; margin-top: 4px; flex: none; }

  .watermark {
    position: absolute; left: 220px; top: 375px; width: 460px; height: 460px;
    background: var(--watermark); border-radius: 90px;
  }
  .signature {
    position: absolute; left: 140px; top: 925px; width: 310px; height: 72px;
    background: var(--signature-tone); border-radius: 6px;
  }
</style>
</head>
<body>
<main class="letterhead">
  <svg class="waves" viewBox="0 0 1282 1812" preserveAspectRatio="none" aria-hidden="true">
    <path class="header-swoosh" fill="var(--swoosh-dark)"
      d="M0,112 C170,45 330,40 500,85 C690,135 840,255 1020,275 C1130,287 1210,262 1282,215 V0 H0 Z"/>
    <path class="header-band" fill="var(--brand-blue)"
      d="M0,0 H1282 V212 C1200,250 1120,265 1020,258 C840,242 690,125 500,72 C330,28 170,38 0,108 Z"/>
    <path class="footer-swoosh" fill="var(--swoosh-dark)"
      d="M10,1660 C200,1588 420,1622 640,1688 C840,1745 960,1778 1060,1778 C1160,1778 1230,1755 1282,1733 L1282,1740 C1230,1764 1150,1790 1060,1791 C950,1792 830,1752 640,1700 C420,1640 200,1600 10,1660 Z"/>
    <path class="footer-band" fill="var(--brand-blue)"
      d="M0,1682 C150,1622 380,1642 600,1702 C800,1757 950,1802 1050,1800 C1150,1798 1230,1772 1282,1750 V1812 H0 Z"/>
  </svg>

  <header class="brand">
    <div class="brand-mark" aria-hidden="true"></div>
    <h1 class="brand-name">Corvane<br>Building<br>Materials</h1>
  </header>

  <address class="contact">
    <div class="contact-item">
      <svg viewBox="0 0 24 24" aria-hidden="true"><path fill="#fff" d="M6.6 10.8a15 15 0 0 0 6.6 6.6l2.2-2.2a1 1 0 0 1 1-.25 11.4 11.4 0 0 0 3.6.57 1 1 0 0 1 1 1V20a1 1 0 0 1-1 1A17 17 0 0 1 3 4a1 1 0 0 1 1-1h3.5a1 1 0 0 1 1 1c0 1.25.2 2.45.57 3.57a1 1 0 0 1-.25 1Z"/></svg>
      <span>044-210 738 564</span>
    </div>
    <div class="contact-item">
      <svg viewBox="0 0 24 24" aria-hidden="true"><rect x="2" y="5" width="20" height="14" fill="none" stroke="#fff" stroke-width="2"/><path d="M2 5l10 8 10-8" fill="none" stroke="#fff" stroke-width="2"/></svg>
      <span>info@corvanebuild.com</span>
    </div>
    <div class="contact-item">
      <svg viewBox="0 0 24 24" aria-hidden="true"><circle cx="12" cy="12" r="10" fill="none" stroke="#fff" stroke-width="2"/><path d="M2 12h20M12 2c3 3 3 17 0 20M12 2c-3 3-3 17 0 20" fill="none" stroke="#fff" stroke-width="1.6"/></svg>
      <span>www.corvanebuild.com</span>
    </div>
    <div class="contact-item">
      <svg viewBox="0 0 24 24" aria-hidden="true"><path fill="#fff" d="M12 2a7 7 0 0 0-7 7c0 5 7 13 7 13s7-8 7-13a7 7 0 0 0-7-7Zm0 9.5A2.5 2.5 0 1 1 12 6.5a2.5 2.5 0 0 1 0 5Z"/></svg>
      <span>218, Harbor Mill Road<br>Westland County, 30871</span>
    </div>
  </address>

  <div class="watermark" aria-hidden="true"></div>

  <div class="signature" role="img" aria-label="Handwritten signature of the sender"></div>
</main>
</body>
</html>
```